Tick Tock Green Frog

I'm looking for one generic business card that be used for four people or would it be easier to get four different design of cards.

I have attached the logo, of the cow. I would also like to use one colour of the cow's legs in the background.

Info for card:
Dana Holcroft
Wrangler of Opportunities
Phone: 044 718 2094
email: dana.holcroft@ticktockgreenfrogs.com.au
Web: www.ticktockgreenfrogs.com.au

Here is some tag lines that could also be used:

"Moo-ving you in the right direction"

"Putting the Tick Tock back into early childhood"
"Where's there is NO bull"

Industry/Entity Type

Business

```html
<!DOCTYPE html>
<html lang="en">
<head>
<meta charset="utf-8">
<title>Tick Tock Green Frog – Business Card</title>
<link href="https://fonts.googleapis.com/css2?family=Acme&family=Open+Sans:wght@400;600;700&display=swap" rel="stylesheet">
<style>
  :root {
    --bg: #e4e5e6;
    --green: #99cc00;
    --green-dark: #6a9e10;
    --orange: #ff6600;
    --brown: #4a2a10;
    --grey: #555555;
    --white: #ffffff;
  }
  * { box-sizing: border-box; margin: 0; padding: 0; }
  html, body {
    width: 1200px; height: 960px; overflow: hidden;
    background: var(--bg);
  }
  .canvas { position: relative; width: 1200px; height: 960px; }

  .card {
    position: absolute; left: 260px; width: 680px; height: 415px;
    overflow: hidden;
    box-shadow: 0 6px 18px rgba(0,0,0,0.18);
  }

  /* Back of card */
  .card--back { top: 45px; background: var(--green); }
  .logo-lockup {
    position: absolute; left: 50%; top: 50%;
    transform: translate(-50%, -50%);
    display: flex; align-items: center; gap: 18px;
  }
  .logo-lockup__mark {
    width: 30px; height: 30px; border-radius: 50%;
    background: var(--brown);
  }
  .logo-lockup__name {
    font-family: "Acme", sans-serif;
    font-size: 50px; color: var(--brown);
    white-space: nowrap;
  }

  /* Front of card */
  .card--front { top: 500px; background: var(--white); }
  .cloud { position: absolute; left: 0; top: 0; width: 240px; height: 310px; }
  .cloud path { fill: var(--orange); }
  .tagline {
    position: absolute; left: 22px; top: 95px; width: 190px;
    font-family: "Acme", sans-serif; font-size: 22px; line-height: 1.3;
    color: var(--white); text-align: center;
  }
  .contact { position: absolute; left: 280px; top: 118px; right: 30px; }
  .contact__name {
    font-family: "Acme", sans-serif; font-size: 38px;
    color: var(--brown); line-height: 1;
  }
  .contact__rule {
    height: 2px; background: var(--orange);
    margin: 10px 0 10px -20px;
  }
  .contact__role {
    font-family: "Open Sans", sans-serif; font-size: 15px;
    letter-spacing: 0.5px; color: var(--grey); text-transform: uppercase;
  }
  .contact__details {
    margin-top: 38px;
    font-family: "Open Sans", sans-serif; font-size: 14.5px;
    color: var(--grey); line-height: 1.45;
  }
  .contact__web {
    font-family: "Open Sans", sans-serif; font-weight: 700;
    font-size: 17px; color: var(--orange); margin-top: 2px;
  }
  .card__band {
    position: absolute; left: 0; right: 0; bottom: 0; height: 18px;
    background: var(--green-dark);
  }
</style>
</head>
<body>
<main class="canvas">

  <section class="card card--back" aria-label="Card back">
    <div class="logo-lockup">
      <span class="logo-lockup__mark"></span>
      <span class="logo-lockup__name">Tick Tock Green Frog</span>
    </div>
  </section>

  <section class="card card--front" aria-label="Card front">
    <svg class="cloud" viewBox="0 0 240 310" aria-hidden="true">
      <path d="M0 0 H190 A34 34 0 0 1 220 40 A34 34 0 0 1 230 100 A34 34 0 0 1 230 165 A34 34 0 0 1 225 230 A34 34 0 0 1 195 285 A34 34 0 0 1 135 300 A34 34 0 0 1 75 300 A40 40 0 0 1 0 295 Z"/>
    </svg>
    <p class="tagline">Putting the Tick Tock back into early childhood</p>

    <div class="contact">
      <h1 class="contact__name">Dana Holcroft</h1>
      <div class="contact__rule"></div>
      <p class="contact__role">Wrangler of Opportunities</p>
      <div class="contact__details">
        <p>P:&nbsp; 044 718 2094</p>
        <p>E:&nbsp; dana.holcroft@ticktockgreenfrogs.com.au</p>
      </div>
      <p class="contact__web">www.ticktockgreenfrogs.com.au</p>
    </div>
    <div class="card__band"></div>
  </section>

</main>
</body>
</html>
```